DATA PROTECTION OFFICER - GENERAL DATA PROTECTION REGULATION

Our network of companies is called : KTV (GDPR-DPO ORLAX).
It is sourced and based in Brussels, Belgium, hosting the EU institutions : designers and enforcers of the GDPR (https://portal.vantreximo.example/info/law/privacy-rules_en).
We are setting up connected, empowered and visionary-interconnected organizations in each country, region or city concerned by the GDPR.
We have developed unique pedagogical methods, programs, instruments (video, softwares,…) and visionary training skills – initially and on a continuous basis – for the DPO & GDPR consultants.
Our motto is : From Challenges to Opportunities.
Our yearning is : developing soulful teams, join forces & talents with our clients.
Our most wanted reward : let us astonish you!
We opt for the best available softwares on the market for project management, data analytics, GDPR compliance, DPO assistance and in general : customer relation and enhanced communication between project members.
We contribute to bringing Artificial Intelligence and Data-Driven Mindsets in enterprises.
We perceive the GDPR as the best opportunity an organization faces to value its “gold” (its data) and offer the solutions to transform them into real-life currencies and assets… MONEY .
I guess my comments need time to be integrated and I provided a lot of text too! I would particularly encourage RW (UK) to take the best out of his several proposals to mix them in the best ONE website! Offering me many graphic elements to use for all my posts/pages... I am a prolix writer :)
Target Market(s)
SME's business leaders, HR and Legal departments, read : https://www.dailyquorvent.example/article/us-cyber-gdpr-dpo/growth-of-the-privacy-officer-role-in-firms-idQX8TR2LM4
Industry/Entity Type
Legal
Coding
Coded - Design and coding required
Number of Pages Required
5+ page
Colors
Designer to choose colors to be used in the design.
Requirements
Must have
- A HUMAN APPROACH
- WE NEED TO SEE HUMANS AND NOT ONLY ROBOTS OR ELECTRONIC DEVICES.
- 1) The DPO/GDPR Logos of the companies:
- https://files.pelmora.example/sh/a1b2c3d4e5f6g7h/AAX9kLmNpQrStUvWxYz0AbCd?dl=0
- https://files.pelmora.example/sh/h7g6f5e4d3c2b1a/AAY8jKlMnOpQrStUvWxYzAbC?dl=0 et DPO : https://files.pelmora.example/sh/q2w3e4r5t6y7u8i/AAZ7hIjKlMnOpQrStUvWxY-z?dl=0
- OR :
- https://files.pelmora.example/sh/z9x8c7v6b5n4m3l/AAW6gHiJkLmNoPqRsTuVwXyZ?dl=0
- AND :
- https://corvilanto.teamdrive.example/sites/all/_layouts/15/guestaccess.aspx?guestaccesstoken=Q4kdpx392MWTZ8RhbyN1Ka7m%2BTcqLwej5spK%2FmUnRQV%3D&folderid=2_7c31d90e24a815f96d02b4613e907a2fc&rev=1&e=9b271cd044716392c5207a44de8117a3
- 2) A surprising but human, clear, simple, white, lightning look!
- 3) WORDPRESS version so that I can edit easily and add text on existing and new pages
- We therefore pass each option and - even more so - through the sieve of this inevitable - and values-generating - ethical evaluation.
- In other words, we are doubly satisfied with EVERY solution:
- 1. As a DPO/consultant and advisor to commercial enterprises or non-profit organisations but necessarily entering into a relationship involving financial flows with the persons concerned; and
- 2. As concerned person: target of the actions envisaged, parent, child, citizen and avatar in our digital lives.
- We put personal data at the centre of our projects and internal meetings, and with clients, we therefore continue the stage of brainstorming, researching and visualising ideas in interaction with the Regulation, by analysing the ethical consequences of each option.
- We choose only solutions that are applicable to the greatest number and therefore satisfy us as citizens of an increasingly connected and digital world. We also see the Regulation as a commercial and marketing opportunity to enhance the value of personal data and develop the confidence of those concerned by respect and security in the processing of such data.
- Our ultimate test: we put ourselves in our children's shoes to test the option considered, then comment on it and evaluate it as a parent.
- NO TO INCOMPREHENSIVE LEGAL TERMS... It is simply prohibited from 25 May for all information to be communicated to the persons concerned by the Regulation!
Nice to have
- - Artificial Intelligence
- - Transhumans
- - Challenges becoming Opportunities
- - a Great Dame who Protects & Reassures (see GDPR logo)
- - Friendly communication - NOT too businesslike/cold/usual
- - Page content is available here in FRENCH then ENGLISH then DUTCH then GERMAN : https://files.pelmora.example/sh/k3j4h5g6f7d8s9a/AAV5fGhIjKlMnOpQrStUvWxY?dl=0
Should not have
- A cold, bankerlike, old economy, dull outlook

```html
<!DOCTYPE html>
<html lang="en">
<head>
<meta charset="utf-8">
<title>GDPR Compliance – Lumera</title>
<link href="https://fonts.googleapis.com/css2?family=Poppins:wght@300;400;500;600;700&display=swap" rel="stylesheet">
<style>
:root{
  --pink:#c8408f;
  --pink-dark:#b0357c;
  --ink:#333340;
  --muted:#555560;
  --white:#ffffff;
  --navy:#0c1a2c;
  --navy-2:#142a40;
  --rule:#bbbbc4;
  --rule-pink:#d99ac0;
}
*{margin:0;padding:0;box-sizing:border-box}
html,body{width:1200px;height:3482px;overflow:hidden}
body{position:relative;background:var(--white);font-family:'Poppins',sans-serif;color:var(--ink)}
.abs{position:absolute}

/* brand lockup: plain circle + name in one colour/weight */
.brand{display:flex;align-items:center;gap:12px;color:var(--pink);font-weight:400;white-space:nowrap}
.brand-dot{border-radius:50%;background:var(--pink);flex:none}
.header-brand{left:86px;top:40px}
.header-brand .brand-dot{width:44px;height:44px}
.header-brand .brand-name{font-size:30px;line-height:1;letter-spacing:1px}

/* hero */
.hero{position:absolute;left:0;top:0;width:1200px;height:615px}
.main-nav a{color:var(--white);text-decoration:none;position:absolute;white-space:nowrap;font-size:13px;letter-spacing:.3px}
.hero-title{left:288px;top:251px;width:622px;height:116px;background:rgba(255,255,255,.78);display:flex;align-items:center;justify-content:center;color:var(--pink);font-size:56px;font-weight:600;letter-spacing:1px}
.slider-dots{left:561px;top:542px;display:flex;gap:5px}
.slider-dots span{width:14px;height:14px;border-radius:50%;border:2px solid var(--white)}
.slider-dots .on{background:var(--pink);border-color:var(--pink)}

/* section headings */
.section-title{left:0;width:1200px;text-align:center;color:var(--pink);font-size:26px;font-weight:400;letter-spacing:.5px}
.title-rule{height:2px;background:var(--rule)}

/* vision cards */
.vision-card{top:803px;width:333px;height:265px;display:flex;align-items:flex-end;justify-content:center;padding-bottom:20px;color:var(--white);font-size:18px;font-weight:600}

/* work process band */
.process-band{left:0;top:1179px;width:1200px;height:202px;background:linear-gradient(90deg,#b23d87,#c95aa0 50%,#b23d87)}
.process-box{left:86px;top:1240px;width:1028px;height:141px;background:var(--white)}

/* steps */
.step-label{font-size:17px;color:var(--ink)}
.step-title{font-size:29px;color:var(--pink);font-weight:400;letter-spacing:.4px}
.step-rule{width:204px;height:1.5px;background:var(--rule-pink)}
.step-text{font-size:16px;line-height:28px;color:var(--muted)}
.step-text.small{font-size:13.5px;line-height:23px}
.step-lead{font-size:15px;font-weight:600;color:var(--pink)}
.step-sub{font-size:15px;font-weight:600;color:var(--pink)}
.btn{display:flex;align-items:center;justify-content:center;background:var(--pink);color:var(--white);font-size:14px;text-decoration:none}
.step-photo{position:absolute}

/* footer */
.site-footer{left:0;top:3189px;width:1200px;height:293px;background:radial-gradient(ellipse at 50% 0%,var(--navy-2),var(--navy) 70%)}
.footer-nav{left:86px;top:3258px;font-size:14px;color:var(--white);white-space:nowrap}
.footer-nav .sep{margin:0 22px}
.copyright{left:86px;top:3332px;font-size:13px;color:var(--white)}
.social{left:368px;top:3330px;display:flex;gap:8px}
.social span{width:30px;height:30px;border-radius:50%;background:var(--pink)}
.footer-brand{left:812px;top:3292px}
.footer-brand .brand-dot{width:78px;height:78px}
.footer-brand .brand-name{font-size:40px;line-height:1;letter-spacing:1px}
</style>
</head>
<body>

<header class="hero">
  <svg class="abs" width="1200" height="615" viewBox="0 0 1200 615" role="img" aria-label="Hero image: a human hand reaching toward a glowing robotic hand in violet light">
    <defs>
      <linearGradient id="heroGrad" x1="0" y1="0" x2="1" y2="1">
        <stop offset="0" stop-color="#3a1a4e"/>
        <stop offset=".45" stop-color="#7a4a96"/>
        <stop offset=".7" stop-color="#4b3a9c"/>
        <stop offset="1" stop-color="#1b1a5c"/>
      </linearGradient>
      <radialGradient id="heroGlow" cx=".55" cy=".25" r=".45">
        <stop offset="0" stop-color="#f4d8f0" stop-opacity=".8"/>
        <stop offset="1" stop-color="#f4d8f0" stop-opacity="0"/>
      </radialGradient>
    </defs>
    <polygon points="0,0 1200,0 1200,555 600,615 0,535" fill="url(#heroGrad)"/>
    <polygon points="0,0 1200,0 1200,555 600,615 0,535" fill="url(#heroGlow)"/>
  </svg>

  <div class="brand header-brand abs">
    <span class="brand-dot"></span>
    <span class="brand-name">LUMERA</span>
  </div>

  <nav class="main-nav abs" style="left:0;top:72px">
    <a style="left:599px">HOME</a>
    <a style="left:680px">WHAT WE DO</a>
    <a style="left:812px">WHO WE ARE</a>
    <a style="left:945px">BLOG</a>
    <a style="left:1024px">CONTACT US</a>
  </nav>

  <h1 class="hero-title abs">GDPR COMPLIANCE</h1>

  <div class="slider-dots abs"><span></span><span></span><span class="on"></span><span></span><span></span></div>
</header>

<h2 class="section-title abs" style="top:715px">OUR VISION TO GDPR COMPLIANCE &amp; DPO MISSIONS</h2>
<div class="title-rule abs" style="left:499px;top:770px;width:202px"></div>

<div class="vision-card abs" style="left:90px;background:radial-gradient(circle at 50% 40%,#8a8a92,#1a1a20 70%)" role="img" aria-label="Illustration of a human head made of metal fragments">Legal Design</div>
<div class="vision-card abs" style="left:434px;background:radial-gradient(circle at 55% 55%,#7a4a8a,#2a0f26 70%)" role="img" aria-label="Abstract network of glowing particle threads">Artificial Intelligence</div>
<div class="vision-card abs" style="left:778px;background:radial-gradient(circle at 45% 40%,#6e6f80,#14151e 70%)" role="img" aria-label="Photo of a person with a robotic arm">Ethics</div>

<div class="process-band abs"></div>
<div class="process-box abs"></div>
<h2 class="section-title abs" style="top:1306px">OUR WORK PROCESS</h2>
<div class="title-rule abs" style="left:499px;top:1352px;width:202px"></div>

<!-- Step 1 -->
<div class="step-label abs" style="left:84px;top:1530px">Step 1</div>
<h3 class="step-title abs" style="left:84px;top:1555px">GRAPHIC TABLE &amp; INTERACTION</h3>
<div class="step-rule abs" style="left:84px;top:1606px"></div>
<p class="step-text abs" style="left:84px;top:1622px;width:590px">The 3 profiles of our teams (IT/cybersecurity Expert - Lawyer - Project Manager) make use of modern tools of communication INTERNALLY and EXTERNALLY: with external clients and partners.</p>
<p class="step-text abs" style="left:84px;top:1734px;width:590px">We use tactile tablets and graphic applications for drawing, mind-mapping, visualization, advanced natural language generation (advanced NLG), video, storytelling,...</p>
<a class="btn abs" style="left:91px;top:1845px;width:139px;height:40px">Read More</a>
<svg class="step-photo" style="left:766px;top:1462px" width="434" height="488" viewBox="0 0 434 488" role="img" aria-label="Photo of a team meeting around a table with laptops, in a triangle frame">
  <defs><linearGradient id="g1" x1="0" y1="0" x2="1" y2="1"><stop offset="0" stop-color="#cfd6dc"/><stop offset=".6" stop-color="#7d8690"/><stop offset="1" stop-color="#3f4650"/></linearGradient></defs>
  <polygon points="22,22 22,466 470,244" fill="url(#g1)" stroke="url(#g1)" stroke-width="40" stroke-linejoin="round"/>
</svg>

<!-- Step 2 -->
<svg class="step-photo" style="left:0;top:1996px" width="434" height="488" viewBox="0 0 434 488" role="img" aria-label="Illustration of a glowing sphere of data light, in a triangle frame">
  <defs><radialGradient id="g2" cx=".6" cy=".45" r=".6"><stop offset="0" stop-color="#f5e3c8"/><stop offset=".35" stop-color="#b07ab0"/><stop offset="1" stop-color="#1c2a5a"/></radialGradient></defs>
  <polygon points="412,22 412,466 10,244" fill="url(#g2)" stroke="url(#g2)" stroke-width="40" stroke-linejoin="round"/>
</svg>
<div class="step-label abs" style="left:478px;top:2064px">Step 2</div>
<h3 class="step-title abs" style="left:478px;top:2090px">HUMAN BY DESIGN</h3>
<div class="step-rule abs" style="left:478px;top:2140px"></div>
<p class="step-lead abs" style="left:478px;top:2162px">EACH solution passes a double test that satisfies us both :</p>
<p class="step-text abs" style="left:478px;top:2214px;width:620px">1.&nbsp;&nbsp;&nbsp;&nbsp;As a DPO/consultant and advisor to commercial enterprises or non-profit organizations but necessarily entering into a relationship involving financial flows with the persons concerned</p>
<p class="step-text abs" style="left:478px;top:2328px;width:620px">2.&nbsp;&nbsp;&nbsp;&nbsp;As a data subject : “target” of the envisaged actions, parent, child, citizen and avatar in our digital lives.</p>
<a class="btn abs" style="left:478px;top:2396px;width:142px;height:40px">Read More</a>

<!-- Step 3 -->
<div class="step-label abs" style="left:84px;top:2628px">Step 3</div>
<h3 class="step-title abs" style="left:84px;top:2653px">VISUALIZATION AND REDACTION</h3>
<div class="step-rule abs" style="left:84px;top:2704px"></div>
<p class="step-text small abs" style="left:84px;top:2722px;width:640px">During the first two stages, we prepared a desirable objective: Communicate visually after an ethical check.<br>Two external solutions (human and artificial) will help us to finalize the communication in a professional and optimal way:</p>
<p class="step-sub abs" style="left:84px;top:2826px">A. Graphic design outsourcing</p>
<p class="step-text small abs" style="left:84px;top:2866px;width:640px">We make online tenders of graphic creations to professionalize the last stage of Legal design, visual, web, video productions...</p>
<p class="step-sub abs" style="left:84px;top:2936px">B. Artificial Intelligence</p>
<p class="step-text small abs" style="left:84px;top:2976px;width:640px">Just as electricity has transformed one industrial sector after another there is so much to be done.</p>
<a class="btn abs" style="left:86px;top:3036px;width:139px;height:42px">Read More</a>
<svg class="step-photo" style="left:766px;top:2560px" width="434" height="488" viewBox="0 0 434 488" role="img" aria-label="Photo of a man touching a digital interface, in a triangle frame">
  <defs><linearGradient id="g3" x1="0" y1="0" x2="1" y2="1"><stop offset="0" stop-color="#b8b4b4"/><stop offset=".5" stop-color="#c49a8e"/><stop offset="1" stop-color="#e9d2cc"/></linearGradient></defs>
  <polygon points="22,22 22,466 470,244" fill="url(#g3)" stroke="url(#g3)" stroke-width="40" stroke-linejoin="round"/>
</svg>

<!-- Footer -->
<footer class="site-footer abs" role="img" aria-label="Dark blue digital network backdrop"></footer>
<nav class="footer-nav abs">Home<span class="sep">|</span>What We Do<span class="sep">|</span>Who We Are<span class="sep">|</span>Blog<span class="sep">|</span>Contact Us</nav>
<div class="copyright abs">LUMERA © 2018 All Rights Reserved.&nbsp;&nbsp;&nbsp;&nbsp;&nbsp;|</div>
<div class="social abs" aria-label="Social links">
  <span></span><span></span><span></span><span></span><span></span>
</div>
<div class="brand footer-brand abs">
  <span class="brand-dot"></span>
  <span class="brand-name">LUMERA</span>
</div>

</body>
</html>
```